Eye-catching Takeaway Coffee Cup & Bag Design For a Vibrant Cafe-Deli

I am developing my company's brand by introducing a splash of colour. I need new takeaway coffee cups (8oz, 10oz & espresso) and paper shopping bags. Plus business cards. (I also need a cafe banner designed for outside my cafe on the street)
Life has been tough for everyone with the Corona Virus, and I want happy, colourful packaging going forward - not the boring black cups and white bags we use at the moment.
I have the exact Pantone references for the colours I want which go in a particular order - a striped pattern. I am looking for a design which incorporates my simple black and white log with the stripes - which looks incredibly eye catching and cool as my customers walk down the street with my cups or bags or receive a delivery from us. I want people to look at our packaging and go 'wow where did that come from..' and google us or check out our Snapgram or Roam Rater etc I don't want anything boring and dated please! Our website is: www.brimwoodcafe.co.uk and Snapgram @brimwoodeatswell which should give you a detailed idea of what we do. Thanks very much!

Target Market(s)

My customers are well educated and have a good disposable income. We are based in Chichester, West Sussex UK.

Contact Information for Business Card

Smart, clear and include the coloured stripes perhaps on one side?

Requirements
Must have
• I am looking for coffee cups and bags that really stand out and can compete with the branding of Cafe Ostra. I want exactly the Pantone colours I have uploaded in exactly the order on the photo of the bag example. However I do not want an exact copy of the logo positioning of the bag in the picture I sent you, please be much more original than this! I need a few key words on the bag as well as my logo (you can loose the circle around my logo its not important) Words such as: Sushi Salad Bowls Curry Bowls Panini Raw Juices Smoothies Organic Coffee Wine & Beer. Please use a font that works really well with my logo - look at my website font.
Nice to have
• Double sided business card please.

```html
<!DOCTYPE html>
<html lang="en">
<head>
<meta charset="utf-8">
<title>Brimwood — Packaging Wrap</title>
<link rel="stylesheet" href="https://fonts.googleapis.com/css2?family=Josefin+Sans:wght@300;400;700&display=swap">
<style>
  :root {
    --tone-mauve: #c984a4;
    --tone-plum: #5a3338;
    --tone-taupe: #665a56;
    --tone-rose: #d98aa8;
    --tone-violet: #5d3b85;
    --tone-slate: #4f605d;
    --tone-raspberry: #e43167;
    --ink-white: #ffffff;
  }
  html, body {
    margin: 0;
    padding: 0;
    width: 1200px;
    height: 535px;
    overflow: hidden;
    background: #ffffff;
  }
  .wrap-design {
    display: block;
    width: 1200px;
    height: 535px;
  }
  .brand-name {
    font-family: "Josefin Sans", sans-serif;
    font-weight: 700;
    font-size: 124px;
    fill: var(--ink-white);
  }
  .tagline {
    font-family: "Josefin Sans", sans-serif;
    font-weight: 400;
    font-size: 38px;
    fill: var(--ink-white);
  }
  .menu-line {
    font-family: "Josefin Sans", sans-serif;
    font-weight: 300;
    font-size: 16px;
    fill: var(--ink-white);
  }
  .brand-dot { fill: var(--ink-white); }
</style>
</head>
<body>
<svg class="wrap-design" viewBox="0 0 1200 535" xmlns="http://www.w3.org/2000/svg">
  <defs>
    <linearGradient id="backdrop-tones" x1="0" y1="0" x2="0" y2="1">
      <stop offset="0" stop-color="var(--tone-mauve)"/>
      <stop offset="0.22" stop-color="var(--tone-plum)"/>
      <stop offset="0.38" stop-color="var(--tone-taupe)"/>
      <stop offset="0.5" stop-color="var(--tone-rose)"/>
      <stop offset="0.64" stop-color="var(--tone-violet)"/>
      <stop offset="0.86" stop-color="var(--tone-slate)"/>
      <stop offset="1" stop-color="var(--tone-raspberry)"/>
    </linearGradient>
  </defs>

  <rect class="backdrop" x="0" y="0" width="1200" height="535" fill="url(#backdrop-tones)"
        role="img" aria-label="Brand colour stripe pattern in mauve, plum, rose, violet, slate and raspberry tones"/>

  <g class="brand-row">
    <circle class="brand-dot" cx="0" cy="202" r="18"/>
    <text class="brand-name" x="300" y="248" text-anchor="middle" textLength="490" lengthAdjust="spacingAndGlyphs">BRIMWOOD</text>
    <circle class="brand-dot" cx="601" cy="202" r="18"/>
    <text class="brand-name" x="900" y="248" text-anchor="middle" textLength="490" lengthAdjust="spacingAndGlyphs">BRIMWOOD</text>
    <circle class="brand-dot" cx="1200" cy="202" r="18"/>
  </g>

  <g class="tagline-row">
    <text class="tagline" x="302" y="305" text-anchor="middle" textLength="384" lengthAdjust="spacing">KITCHEN. BAR. SHOP.</text>
    <text class="tagline" x="902" y="305" text-anchor="middle" textLength="384" lengthAdjust="spacing">KITCHEN. BAR. SHOP.</text>
  </g>

  <text class="menu-line" x="38" y="476" textLength="1122" lengthAdjust="spacing">SUSHI • CURRIES • SALADS • PANINI • RAW JUICES • SMOOTHIES • ORGANIC COFFEE • COCKTAILS • WINE • BEER</text>
</svg>
</body>
</html>
```